Redesign of the Klammbrot label

I am a pharmacist and sell a bitters called "Klammbrot". I would like to revise and modernize the current logo of my "Klammbrot". I have attached a photo of the current label. I have different bottle sizes with different label sizes, but for now I will only need one label for the 700ml size:
20ml 36x47mm
40ml 45x62mm
200ml 70x91mm
350ml 70x98mm
500ml 70x110mm
700ml 87x119mm
The Uffe is a small stream that runs through our town. The Klammbrot is a play on words that takes up the mysticism of the Harz, as a spirit can of course also be a schnapps. I like the mysticism and rough nature of the Harz in connection with the product. I have attached a logo suggestion that I once had an AI design. But I am very open to new ideas. A connection to my pharmacy does not necessarily have to be recognizable. VG, K. Brandis

Target Market(s)

End consumers, gastronomy, restaurants, hotels

```html
<!DOCTYPE html>
<html lang="de">
<head>
<meta charset="utf-8">
<title>Klammbrot Bitterlikör – Etikett 700 ml</title>
<link rel="stylesheet" href="https://fonts.googleapis.com/css2?family=Rye&family=Italiana&family=Montserrat:wght@700&family=Federo&display=swap">
<style>
  :root {
    --gold: #d4a766;
    --gold-deep: #b8894c;
    --tan: #dcb67c;
    --ink: #1c2a22;
    --forest: #1f3b33;
    --forest-dark: #0f1f1b;
    --cream: #f3ead8;
    --white: #ffffff;
  }
  html, body { margin: 0; padding: 0; overflow: hidden; background: #e9e4da; }
  .label {
    position: relative;
    width: 877px; height: 1200px;
    background: var(--tan);
    overflow: hidden;
    font-family: "Italiana", serif;
  }
  .label__field {
    position: absolute; left: 12px; top: 12px; right: 12px; bottom: 12px;
    background: radial-gradient(ellipse at 50% 35%, #2f5a4d 0%, var(--forest) 45%, var(--forest-dark) 100%);
  }
  .label__frame { position: absolute; inset: 0; }
  .label__flourish {
    position: absolute; left: 100px; top: 180px; width: 670px; height: 330px;
    border-radius: 50%;
    background: radial-gradient(ellipse, rgba(212,167,102,0.08), rgba(212,167,102,0) 70%);
  }
  .brand {
    position: absolute; top: 68px; left: 0; width: 100%;
    text-align: center;
    font-family: "Rye", serif; font-size: 56px;
    color: var(--gold); letter-spacing: 1px;
  }
  .kicker {
    position: absolute; top: 188px; left: 192px;
    font-family: "Montserrat", sans-serif; font-weight: 700;
    font-size: 24px; letter-spacing: 5px; color: var(--cream);
  }
  .title {
    position: absolute; top: 270px; left: 0; width: 100%; margin: 0;
    text-align: center;
    font-family: "Rye", serif; font-size: 96px; font-weight: 400;
    color: var(--gold); letter-spacing: 2px;
    transform: rotate(-4deg);
  }
  .subtitle {
    position: absolute; top: 420px; left: 335px;
    font-family: "Montserrat", sans-serif; font-weight: 700;
    font-size: 27px; letter-spacing: 6px; color: var(--white);
    transform: rotate(-7deg); transform-origin: left center;
  }
  .banner { position: absolute; left: 128px; top: 500px; width: 616px; height: 96px; }
  .banner__text { font-family: "Montserrat", sans-serif; font-weight: 700; font-size: 25px; fill: var(--ink); }
  .copy {
    position: absolute; top: 652px; left: 70px; right: 70px;
    text-align: center; color: var(--cream);
    font-size: 24px; line-height: 34px; margin: 0;
  }
  .origin {
    position: absolute; top: 856px; left: 0; width: 100%;
    text-align: center; color: var(--cream);
    font-family: "Federo", serif; font-size: 30px; line-height: 39px; margin: 0;
  }
  .divider { position: absolute; top: 982px; left: 348px; width: 180px; height: 22px; }
  .contact {
    position: absolute; top: 1016px; left: 0; width: 100%;
    text-align: center; color: var(--cream);
    font-family: "Federo", serif; font-size: 22px; line-height: 29px; margin: 0;
  }
  .contact__lot { color: var(--gold); }
  .seal {
    position: absolute; width: 124px; height: 124px; border-radius: 50%;
    border: 2px solid var(--gold); box-sizing: border-box;
    display: flex; flex-direction: column; align-items: center; justify-content: center;
    color: var(--gold); font-family: "Federo", serif;
  }
  .seal::after {
    content: ""; position: absolute; inset: 5px; border-radius: 50%;
    border: 1px solid var(--gold);
  }
  .seal--volume { left: 57px; top: 919px; }
  .seal--abv { left: 689px; top: 910px; }
  .seal__value { font-size: 46px; line-height: 44px; }
  .seal__unit { font-size: 22px; }
</style>
</head>
<body>
<main class="label">
  <div class="label__field" role="img" aria-label="Nebliger dunkler Tannenwald des Harzes als Hintergrund"></div>

  <svg class="label__frame" width="877" height="1200" viewBox="0 0 877 1200" aria-hidden="true">
    <rect x="30" y="30" width="817" height="1140" fill="none" stroke="var(--white)" stroke-width="2"/>
    <rect x="38" y="38" width="801" height="1124" fill="none" stroke="var(--gold)" stroke-width="1.5"/>
    <rect x="46" y="46" width="785" height="1108" fill="none" stroke="var(--gold)" stroke-width="1"/>
    <rect x="196" y="55" width="486" height="104" rx="50" fill="var(--ink)" stroke="var(--gold)" stroke-width="3"/>
    <line x1="390" y1="205" x2="650" y2="205" stroke="var(--gold)" stroke-width="2"/>
    <line x1="300" y1="390" x2="720" y2="360" stroke="var(--gold)" stroke-width="1"/>
    <line x1="330" y1="458" x2="650" y2="412" stroke="var(--gold)" stroke-width="1"/>
  </svg>
  <div class="label__flourish" role="img" aria-label="Goldene Zierranken rund um den Produktnamen"></div>

  <div class="brand">Hohenklammer</div>
  <div class="kicker">ERLESENER</div>
  <h1 class="title">KLAMMBROT</h1>
  <div class="subtitle">BITTERLIKÖR</div>

  <svg class="banner" viewBox="0 0 616 96" aria-hidden="true">
    <defs>
      <path id="bannerArc" d="M36 70 Q308 20 580 70"/>
    </defs>
    <path d="M6 50 Q308 -4 610 50 L610 88 Q308 36 6 88 Z" fill="var(--gold)" stroke="var(--ink)" stroke-width="3" stroke-linejoin="round"/>
    <circle cx="20" cy="68" r="5" fill="var(--ink)"/>
    <circle cx="596" cy="68" r="5" fill="var(--ink)"/>
    <text class="banner__text"><textPath href="#bannerArc" startOffset="50%" text-anchor="middle" textLength="500" lengthAdjust="spacing">NACH ALTER APUTHEKERKUNST</textPath></text>
  </svg>

  <p class="copy">Eine Zubereitung nach höchst geheimem Rezept. Sei sei<br>empfohlen zum Genuss nach einem guten Mahl.<br>Aufs Feinste zubereitet mit geistigen Auszügen von Enzian,<br>Kalmus, Malabar-Kardamom und anderen wertvollen<br>Zutaten.</p>

  <p class="origin">Aus der<br>St. Odilien Apotheke<br>Hohenklamm</p>

  <svg class="divider" viewBox="0 0 180 22" aria-hidden="true">
    <line x1="0" y1="11" x2="72" y2="11" stroke="var(--gold)" stroke-width="2"/>
    <line x1="108" y1="11" x2="180" y2="11" stroke="var(--gold)" stroke-width="2"/>
    <rect x="81" y="2" width="18" height="18" transform="rotate(45 90 11)" fill="none" stroke="var(--gold)" stroke-width="2"/>
  </svg>

  <p class="contact">Dr. K. Brandis<br>Lindenweg 12, 37449 Hohenklamm<br>Tel. 05529-4418<br><span class="contact__lot">Kräuterlikör chininhaltig L4170925</span></p>

  <div class="seal seal--volume"><span class="seal__value">700</span><span class="seal__unit">ML</span></div>
  <div class="seal seal--abv"><span class="seal__value">34%</span><span class="seal__unit">VOL.</span></div>
</main>
</body>
</html>
```